New enterprise - Swiss candle distributor wanting exciting vintage retro-themed packaging

We are an interiors and decorative product distributor in Switzerland and we are developing a new range of scented candles. We are looking for vintage designs for packaging labels for 5 new scented candles all which have a vintage boat /nauticaltheme but should be slightly different for each fragrance. Inspiration from faded colors, muted tones, retro, industrial, sea-dog'esque packaging that has been around the world. Also happy with vintage merchant/mercantile themes from the old spice trade etc. Open to anything nautical vintage.There are two labels per candle - one to be 100mm/260mmcm wrap around tube packaging, the other to be circular diameter of 45mm for lid. The final design should tell a vintage story but be feminine enough for the candle buying market here (predominantly female). Thank you for your help in this. A few pixel vault images attached for thoughts.

Target Market(s)

Female, interiors fans, upmarket, discerning, like quality, like quirky and unusual, not brash or bold, time worn themes.

Industry/Entity Type

Nautical

Font styles to use
Script

Requirements
Must have
• vintage, retro, muted, stylish, nautical/boat/sea theme
Nice to have
• The Velmora Tide logo added (www.velmoratide.example) but in muted tones.
Should not have
• loud, modernistic etc.

```html
<!DOCTYPE html>
<html lang="en">
<head>
<meta charset="utf-8">
<title>Salt on the Decks – candle labels</title>
<link href="https://fonts.googleapis.com/css2?family=Della+Respira&display=swap" rel="stylesheet">
<style>
  :root {
    --backdrop: #5f5f54;
    --cream: #f5e6c1;
    --cream-light: #fdf6d8;
    --peach: #f8bf7c;
    --butter: #fcdc9c;
    --orange: #e0561e;
    --maroon: #6e2b2c;
  }
  html, body {
    margin: 0;
    padding: 0;
    width: 1200px;
    height: 1000px;
    overflow: hidden;
    background: var(--backdrop);
  }
  .canvas { display: block; width: 1200px; height: 1000px; }
  .label-type {
    font-family: "Della Respira", "Georgia", serif;
    fill: var(--maroon);
    text-anchor: middle;
  }
  .brand-name {
    font-family: "Della Respira", "Georgia", serif;
    fill: var(--maroon);
    text-anchor: middle;
  }
</style>
</head>
<body>
<svg class="canvas" viewBox="0 0 1200 1000" xmlns="http://www.w3.org/2000/svg">
  <defs>
    <clipPath id="lid-clip"><circle cx="600" cy="267" r="112"/></clipPath>
    <linearGradient id="lid-sea" x1="0" y1="0" x2="0" y2="1">
      <stop offset="0" stop-color="#f5e6c1"/>
      <stop offset="0.55" stop-color="#f5e6c1"/>
      <stop offset="0.7" stop-color="#f8c98a"/>
      <stop offset="1" stop-color="#fdf0cc"/>
    </linearGradient>
    <linearGradient id="wrap-sea" x1="0" y1="0" x2="0" y2="1">
      <stop offset="0" stop-color="#f5e6c1"/>
      <stop offset="0.5" stop-color="#f5e6c1"/>
      <stop offset="0.72" stop-color="#f9cf92"/>
      <stop offset="1" stop-color="#fdf3d2"/>
    </linearGradient>
  </defs>

  <!-- Lid label -->
  <g class="lid-label">
    <circle cx="600" cy="267" r="137" fill="var(--cream-light)"/>
    <rect class="lid-scene" x="488" y="155" width="224" height="224" clip-path="url(#lid-clip)"
          fill="url(#lid-sea)" role="img" aria-label="Soft rolling sea waves in peach and butter tones"/>
    <circle class="lid-frame" cx="600" cy="267" r="115" fill="none" stroke="var(--orange)" stroke-width="7"/>
    <circle cx="600" cy="196" r="4" fill="var(--orange)"/>
    <text class="brand-name" x="600" y="214" font-size="11">Velmora Tide</text>
    <text class="label-type" x="600" y="262" font-size="38">Salt</text>
    <text class="label-type" x="598" y="290" font-size="26">on the</text>
    <text class="label-type" x="597" y="345" font-size="50">DECKS</text>
  </g>

  <!-- Wrap-around label -->
  <g class="wrap-label">
    <rect class="wrap-scene" x="253" y="533" width="694" height="337" fill="url(#wrap-sea)"
          role="img" aria-label="Soft rolling sea waves in peach and butter tones"/>
    <rect class="edge-band" x="253" y="533" width="694" height="22" fill="var(--orange)"
          role="img" aria-label="Orange zigzag edge pattern"/>
    <rect class="edge-band" x="253" y="848" width="694" height="22" fill="var(--orange)"
          role="img" aria-label="Orange zigzag edge pattern"/>

    <rect class="title-plaque" x="402" y="640" width="398" height="178" rx="14"
          fill="var(--cream-light)" stroke="var(--orange)" stroke-width="5"/>
    <circle class="brand-seal" cx="597" cy="607" r="29" fill="var(--cream-light)" stroke="var(--orange)" stroke-width="4"/>
    <text class="brand-name" x="597" y="611" font-size="9">Velmora Tide</text>

    <text class="label-type" x="610" y="705" font-size="50">Salt</text>
    <text class="label-type" x="605" y="737" font-size="34">on the</text>
    <text class="label-type" x="608" y="805" font-size="70" letter-spacing="6">DECKS</text>
  </g>
</svg>
</body>
</html>
```